依頼詳細
高級住宅地、オフィス街を対象に配るA4チラシ(片面)になります。高級感溢れるデザインをお願いいたします。
印刷はミドリカゼを使用する予定です。入稿可能なAiファイルでの作成をお願いいたします。
https://midorikaze-example.jp/dataguide/

色選びはカラーパレットをご使用ください。
記載項目
記載内容は添付のワードファイルをご参照ください。
講師プロフィール用の写真は仮の写真です。決定いたしまた方に後ほど実際に使用いただく写真をお渡しいたします。
イメージ画像を1枚添付しておりますが、使用はお任せいたします。
サイズ
A4
ページ数
片面
希望イメージ
シンプル 複雑
単色 カラフル
暗い 明るい
日常 高級
遊び心 厳粛
未来的 伝統的
女性的 男性的
希望する色
黄・オレンジ系、青系、無彩色系
納品ファイル
• イラストレーター形式 (.ai)
補足説明
当初の設定ミスで募集期間5日間としていましたが、3日間に訂正いたします。
期間が短くなりますが、どうぞよろしくお願いいたします。
報酬金額変更いたしました。
どうぞよろしくお願いいたします。
提出ファイル形式についての追記です。
採用に至った場合は、そのまま入稿できるAiファイルと後に文字を編集する予定があるためテキストをアウトライン化する前(テキスト部分が後に編集できるもの)のファイルの2種類の提出をお願いいたします。可能であればWindows Adobe Illustrator CS4対応のファイル形式でお願いします。また、特殊なフォントをご使用の場合は一緒にご提出願います。
お手数おかけいたしますがよろしくお願いいたします。

ターゲットを意識した画像の使用、レイアウト、高級感とすべてよかったです。

この度はコンペにご参加いただきありがとうございました。
予想以上に多くの提案をいただきまして大変感謝いたしております。
多数の素晴らしいご提案から選ぶのに時間がかかりまして、
お待たせいたしましたことをお詫び申し上げます。
また、機会がございましたらどうぞよろしくお願いいたします。

```html
<!DOCTYPE html>
<html lang="ja">
<head>
<meta charset="utf-8">
<title>LUMEA 英会話レッスン</title>
<link rel="stylesheet" href="https://fonts.googleapis.com/css2?family=Shippori+Mincho:wght@500;700;800&family=Noto+Serif+JP:wght@400;600;700&display=swap">
<style>
:root{
  --ink:#141414;
  --ink-soft:#2b2b2b;
  --paper:#f7f6f2;
  --silver-hi:#f2f2f2;
  --silver-lo:#8d8d8d;
  --gold:#c9a45a;
  --muted:#4a4a4a;
  --rule:#bdbdbd;
}
*{box-sizing:border-box;margin:0;padding:0}
html,body{width:859px;height:1200px;overflow:hidden}
body{
  font-family:"Noto Serif JP",serif;
  color:var(--ink);
  background:linear-gradient(180deg,#2a2a2a 0%,#111 30%,#1c1c1c 60%,#0e0e0e 100%);
  position:relative;
}
.backdrop{position:absolute;inset:0;background:repeating-linear-gradient(180deg,rgba(255,255,255,.03) 0 3px,rgba(0,0,0,.05) 3px 7px)}
.tagline{position:absolute;top:10px;left:0;width:100%;text-align:center;color:var(--silver-hi);
  font-family:"Shippori Mincho",serif;font-weight:700;font-size:20px;letter-spacing:2px}
.brand{position:absolute;left:120px;top:92px;width:180px;display:flex;align-items:center;gap:10px}
.brand-mark{width:18px;height:18px;background:var(--silver-hi);flex:none}
.brand-name{font-family:"Shippori Mincho",serif;font-weight:700;font-size:34px;line-height:40px;color:var(--silver-hi);letter-spacing:2px}
.subtitle{position:absolute;left:300px;top:52px;color:var(--silver-hi);font-family:"Shippori Mincho",serif;font-weight:700;font-size:24px;letter-spacing:2px}
.title{position:absolute;left:330px;top:86px;font-family:"Shippori Mincho",serif;font-weight:800;
  font-size:60px;line-height:68px;letter-spacing:6px;
  background:linear-gradient(180deg,#fff,#9a9a9a 55%,#e6e6e6);-webkit-background-clip:text;background-clip:text;color:transparent}
.intro{position:absolute;left:34px;top:248px;width:796px;height:40px;background:rgba(255,255,255,.9);
  font-size:11px;line-height:18px;padding:2px 12px;color:var(--ink)}
.limited{position:absolute;left:34px;top:294px;height:24px;display:flex;align-items:center;gap:12px}
.limited-tab{background:var(--paper);font-family:"Shippori Mincho",serif;font-weight:700;font-size:15px;padding:2px 16px}
.limited-note{color:var(--silver-hi);font-size:10px;width:660px;line-height:14px;white-space:nowrap;overflow:hidden}
.panel{position:absolute;background:var(--paper);padding:10px 14px;font-size:11px;line-height:18px}
.panel-head{background:var(--ink-soft);color:#fff;font-family:"Shippori Mincho",serif;font-weight:700;font-size:15px;
  margin:-10px -14px 8px;padding:5px 14px;border-bottom:2px solid var(--gold)}
.panel ul{list-style:none}
.panel li{padding-left:14px;position:relative;margin-bottom:3px}
.panel li::before{content:"";position:absolute;left:2px;top:7px;width:6px;height:6px;background:var(--gold)}
.why{left:34px;top:320px;width:424px;height:240px}
.lessons{left:34px;top:566px;width:424px;height:232px}
.pricing{left:34px;top:806px;width:424px;height:182px}
.contact{left:34px;top:996px;width:424px;height:150px}
.teacher{left:472px;top:320px;width:358px;height:372px}
.teacher-text{width:170px}
.teacher-photo{position:absolute;right:14px;top:44px;width:160px;height:250px;background:linear-gradient(180deg,#6a6258,#3a342f)}
.message{left:472px;top:700px;width:358px;height:98px}
.message-head{font-family:"Shippori Mincho",serif;font-weight:700;font-size:13px;margin-bottom:4px}
.message-quote{font-style:italic;font-size:12px}
.faq{left:472px;top:806px;width:358px;height:340px}
.faq dt{font-weight:700}
.faq dd{margin-bottom:6px;color:var(--muted)}
table{width:100%;border-collapse:collapse}
td{border-bottom:1px solid var(--rule);padding:3px 2px}
td.price{text-align:right;font-weight:700}
.contact-line{display:flex;align-items:center;gap:8px;font-size:13px;margin-top:6px}
.contact-line svg{width:16px;height:16px;flex:none}
.tel{font-size:22px;font-weight:700;font-family:"Shippori Mincho",serif}
</style>
</head>
<body>
<div class="backdrop" role="img" aria-label="黒い木目調のテクスチャ背景"></div>

<p class="tagline">全てに於いて最高品質を求める貴方へ！</p>
<div class="brand"><span class="brand-mark"></span><span class="brand-name">LUMEA</span></div>
<p class="subtitle">ワンランク上の完全プライベート</p>
<h1 class="title">英会話<br>レッスン</h1>

<p class="intro">LUMEAは、経営者、会社役員、議員、医師、ニュースキャスター等のビジネスの世界で活躍される方々の為の完全プライベート英会話レッスンです。<br>高級住宅地のご自宅や職場など、お客様のご都合の良い場所で質の高いレッスンを提供いたします。</p>

<div class="limited">
  <span class="limited-tab">限定案内</span>
  <p class="limited-note">本チラシをご覧の方限定で、初回体験レッスンを特別価格にてご案内いたします。定員になり次第、受付終了となります。</p>
</div>

<section class="panel why">
  <h2 class="panel-head">なぜ、ジャックのレッスンはこんなに人気なのか？</h2>
  <ul>
    <li>完全マンツーマンで、お客様の目的とレベルに合わせたオーダーメイドの内容です。</li>
    <li>ビジネス会議、商談、プレゼンテーション、会食など実践的な場面を想定します。</li>
    <li>ご自宅、オフィス、ホテルラウンジなどご指定の場所へ講師が伺います。</li>
    <li>多忙な方でも続けられるよう、早朝や夜間のレッスンにも柔軟に対応します。</li>
    <li>守秘義務を徹底し、プライバシーに配慮した環境でご受講いただけます。</li>
    <li>国際舞台で通用する品格ある英語表現とマナーを身につけられます。</li>
  </ul>
</section>

<section class="panel lessons">
  <h2 class="panel-head">レッスン案内</h2>
  <ul>
    <li>1回60分（90分・120分コースもご用意しております）</li>
    <li>場所：ご自宅、オフィス、ホテル等ご指定の場所</li>
    <li>時間：平日・土日祝 7:00〜22:00の間でご相談</li>
    <li>内容：ビジネス英会話、交渉、スピーチ、日常会話</li>
    <li>対象：初心者から上級者まで、どなたでも</li>
    <li>オンラインレッスンにも対応しております</li>
  </ul>
</section>

<section class="panel pricing">
  <h2 class="panel-head">料金</h2>
  <table>
    <tr><td>初回体験レッスン（60分）</td><td class="price">5,000円</td></tr>
    <tr><td>通常レッスン（60分）</td><td class="price">12,000円</td></tr>
    <tr><td>月4回コース（60分×4）</td><td class="price">44,000円</td></tr>
    <tr><td>入会金</td><td class="price">20,000円</td></tr>
  </table>
  <p style="margin-top:4px;font-size:10px;color:var(--muted)">※表示価格は税別です。出張交通費は別途頂戴いたします。</p>
</section>

<section class="panel contact">
  <h2 class="panel-head">お問い合わせ</h2>
  <p class="contact-line">
    <svg viewBox="0 0 24 24" aria-hidden="true"><path fill="#141414" d="M6.6 10.8a15 15 0 0 0 6.6 6.6l2.2-2.2a1 1 0 0 1 1-.25 11.4 11.4 0 0 0 3.6.57 1 1 0 0 1 1 1V20a1 1 0 0 1-1 1A17 17 0 0 1 3 4a1 1 0 0 1 1-1h3.5a1 1 0 0 1 1 1c0 1.25.2 2.45.57 3.6a1 1 0 0 1-.25 1z"/></svg>
    <span class="tel">0120-555-0148</span>
  </p>
  <p class="contact-line">E-mail：info@lumea-english.jp</p>
  <p class="contact-line" style="font-size:11px">受付時間 9:00〜20:00（年中無休）</p>
</section>

<section class="panel teacher">
  <h2 class="panel-head">講師ジャック・モリス紹介</h2>
  <div class="teacher-text">
    <p>ロンドン出身。名門大学にて言語学を専攻後、国際金融機関で通訳として勤務。</p>
    <p style="margin-top:6px">来日後は15年以上にわたり、企業経営者や政治家、医師など各界のリーダーに英語を指導。</p>
    <p style="margin-top:6px">丁寧で品のある指導に定評があり、多くの受講者から厚い信頼を得ている。</p>
  </div>
  <div class="teacher-photo" role="img" aria-label="スーツ姿の講師ジャック・モリスのプロフィール写真"></div>
</section>

<section class="panel message">
  <p class="message-head">講師ジャック・モリスからのメッセージ</p>
  <p class="message-quote">"My goal is to make the country of Japan stronger, one person at a time."</p>
  <p>「私の夢は、一人ずつ日本をより強い国にすることです。」</p>
</section>

<section class="panel faq">
  <h2 class="panel-head">FAQ</h2>
  <dl>
    <dt>Q. 英語が全く話せなくても大丈夫ですか？</dt>
    <dd>A. はい。初心者の方にも分かりやすく、丁寧に基礎からご指導いたします。</dd>
    <dt>Q. レッスンの日時は変更できますか？</dt>
    <dd>A. 前日までにご連絡いただければ、無料で振替が可能です。</dd>
    <dt>Q. 家族で一緒に受講できますか？</dt>
    <dd>A. ご家族やご同僚との少人数レッスンも承ります。</dd>
    <dt>Q. 支払い方法は何がありますか？</dt>
    <dd>A. 銀行振込、またはカードでのお支払いが可能です。</dd>
  </dl>
</section>
</body>
</html>
```